Marigold Compass One Pager

We are looking for an introductory one-pager to tell potential customers about our corporate training program. It is called Marigold Compass. Please see the added files below for detailed specs and requirements. Thank you!

Reason: Hi All, We are extending the project by a day, since we had slow submissions over the weekend. We are looking for a design that is pleasing/modern in look and feel - I think that we would prefer it to look artistic rather than corporate or industrial. I"knew to this, so please forgive me if my directions are vague, and please feel free to reach out for feedback.

Training

```html
<!DOCTYPE html>
<html lang="en">
<head>
<meta charset="utf-8">
<title>Marigold Compass – Brochure</title>
<link rel="stylesheet" href="https://fonts.googleapis.com/css2?family=Didact+Gothic&display=swap">
<style>
  :root {
    --bg: #f2f2f2;
    --mist: #d8d8de;
    --sky: #0a8ad8;
    --ink: #141414;
    --night: #0d0d0f;
    --paper-white: #ffffff;
    --listen-blue: #2aa7e8;
  }
  * { box-sizing: border-box; margin: 0; padding: 0; }
  html, body {
    width: 1200px; height: 1033px; overflow: hidden;
    background: var(--bg);
    font-family: "Didact Gothic", "Century Gothic", sans-serif;
    color: var(--ink);
  }
  .canvas { position: relative; width: 1200px; height: 1033px; }

  .page {
    position: absolute; width: 370px; height: 530px; top: 251px;
    background: var(--sky); overflow: hidden;
    box-shadow: 0 6px 18px rgba(0,0,0,.18);
  }
  .spread { position: absolute; left: 30px; top: 251px; width: 740px; height: 530px; box-shadow: 0 6px 18px rgba(0,0,0,.18); }
  .spread .page { top: 0; box-shadow: none; }
  .page--left { left: 0; }
  .page--right { left: 370px; }
  .page--left::before, .page--right::before {
    content: ""; position: absolute; left: 0; top: 0; width: 370px; height: 230px;
    background: var(--mist);
  }
  .page--left::before { clip-path: path("M0,0 L370,0 L370,150 C260,140 130,160 0,212 Z"); }
  .page--right::before { clip-path: path("M0,0 L370,0 L370,215 C280,190 150,160 0,150 Z"); }
  .spread-fold { position: absolute; left: 369px; top: 0; width: 2px; height: 530px; background: rgba(0,0,0,.12); }

  .abs { position: absolute; }
  .small { font-size: 9.5px; line-height: 1.2; }
  .center { text-align: center; }

  .intro { left: 30px; top: 34px; width: 310px; font-size: 10px; line-height: 1.25; }
  .intro p + p { margin-top: 12px; }

  .badge {
    position: absolute; border-radius: 50%; background: var(--night);
    color: var(--paper-white); display: flex; flex-direction: column;
    align-items: center; justify-content: center; text-align: center;
    font-size: 8.5px; line-height: 1.15;
  }
  .badge p + p { margin-top: 6px; }
  .badge--change { left: 18px; top: 200px; width: 92px; height: 92px; padding: 8px; }
  .tagline { left: 124px; top: 226px; width: 230px; color: var(--paper-white); font-style: italic; font-size: 12.5px; line-height: 1.2; text-align: center; }

  .questions { left: 22px; top: 302px; width: 336px; }
  .questions-lead { margin-bottom: 6px; }
  .process { left: 22px; top: 414px; width: 336px; }
  .skills { left: 22px; top: 438px; width: 336px; }
  .skills ul { list-style: none; margin-left: 80px; }

  .questions--top { left: 20px; top: 24px; width: 330px; }

  .badge--value { left: 24px; top: 196px; width: 100px; height: 100px; padding: 10px; font-size: 9.5px; }
  .dot { position: absolute; border-radius: 50%; background: var(--night); }
  .dot--mid { left: 62px; top: 322px; width: 80px; height: 80px; }
  .dot--low { left: 40px; top: 426px; width: 64px; height: 64px; }
  .value-list { left: 150px; top: 200px; width: 200px; list-style: none; }

  .cover { left: 800px; }
  .cover-band { position: absolute; left: 0; top: 0; width: 370px; height: 210px; background: var(--night); }
  .cover-photo {
    position: absolute; left: 210px; top: 18px; width: 160px; height: 180px;
    background: radial-gradient(ellipse at 55% 45%, #d6dbe4 0%, #8e96a4 40%, #2b2f36 80%, var(--night) 100%);
  }
  .cover-wave { position: absolute; left: 0; top: 0; }
  .listen { left: 28px; top: 52px; color: var(--listen-blue); }
  .listen-word { font-size: 28px; letter-spacing: 1px; }
  .listen-line { font-size: 12.5px; margin-top: 2px; }
  .listen-line--one { margin-left: 42px; }
  .cover-intro { left: 28px; top: 236px; width: 314px; font-size: 11.5px; line-height: 1.2; }
  .cover-lead { left: 20px; top: 318px; width: 330px; font-size: 12.5px; }
  .product-name { left: 20px; top: 342px; width: 330px; font-size: 44px; line-height: 0.95; font-weight: 400; text-align: center; color: var(--ink); text-transform: uppercase; letter-spacing: 1px; }
  .cover-outro { left: 28px; top: 452px; width: 314px; font-size: 11.5px; line-height: 1.2; }
</style>
</head>
<body>
<main class="canvas">

  <section class="spread" aria-label="Inside spread">
    <article class="page page--left">
      <div class="abs intro center">
        <p>We have 40 years of proven success creating dialogue-based solutions to some of the worlds most entrenched and vexing problems.</p>
        <p>Our program is a 3 week programme held once a week at your place of work.</p>
        <p>Our program is a 3 week programme held once a week at your place of work.</p>
      </div>

      <div class="badge badge--change">
        <p>Something needs to change.</p>
        <p>Do you have the tools to get started?</p>
      </div>
      <p class="abs tagline">In just one hour, we went beyond months of small talk...</p>

      <div class="abs questions small">
        <p class="questions-lead">If you have ever asked yourself any of these questions, we can help you:</p>
        <p>What's the most frustrating thing about your job?</p>
        <p>How can we get traction on our companies most difficult problems?</p>
        <p>How do we ask the right questions to make positive changes?</p>
        <p>I want everyone to bring their authentic self to work</p>
        <p>I want to finally gain traction around that tired problem that has been plaguing my organization</p>
        <p>How can I encourage and enable flow of information so that people can work across differences and do their best?</p>
      </div>
      <p class="abs process small">The Marigold Compass Process is a results-based, step by step process</p>
      <div class="abs skills small">
        <p>You will learn essential life-skills thats</p>
        <ul>
          <li>Inherently Energizing</li>
          <li>Community Oriented</li>
          <li>Relationship Enhancing</li>
          <li>Culture Building</li>
          <li>Silo busting</li>
          <li>Simple But Challenging</li>
        </ul>
      </div>
    </article>

    <article class="page page--right">
      <div class="abs questions--top small center">
        <p>What's the most frustrating thing about your job?</p>
        <p>How can we get traction on our companies most difficult problems?</p>
        <p>How do we ask the right questions to make positive changes?</p>
        <p>I want everyone to bring their authentic self to work</p>
        <p>I want to finally gain traction around that tired problem that has been plaguing my organization</p>
        <p>How can I encourage and enable flow of information so that people can work across differences and do their best?</p>
        <p>What's the most frustrating thing about your job?</p>
        <p>How can we get traction on our companies most difficult problems?</p>
        <p>How do we ask the right questions to make positive changes?</p>
      </div>

      <div class="badge badge--value"><p>How Marigold Compass Initiatives Add Value:</p></div>
      <div class="dot dot--mid"></div>
      <div class="dot dot--low"></div>

      <ul class="abs value-list small center">
        <li>Super charges your conversations</li>
        <li>Creates a shared vision</li>
        <li>Transforms relationships</li>
        <li>Empowers people to design change</li>
        <li>Creates lasting momentum</li>
        <li>Delivers measurable results</li>
        <li>Supports inclusive teams</li>
        <li>Drives real engagement</li>
      </ul>
    </article>

    <div class="spread-fold"></div>
  </section>

  <article class="page cover" aria-label="Front cover">
    <div class="cover-band"></div>
    <div class="cover-photo" role="img" aria-label="Close-up photograph of a human ear in cool grey light"></div>
    <svg class="cover-wave" width="370" height="530" viewBox="0 0 370 530" aria-hidden="true">
      <path d="M0,190 C90,205 200,215 370,178 L370,530 L0,530 Z" fill="var(--sky)"/>
    </svg>
    <div class="abs listen">
      <p class="listen-word">LISTEN</p>
      <p class="listen-line listen-line--one">deeply enough</p>
      <p class="listen-line">to be changed by what you hear</p>
    </div>
    <p class="abs cover-intro center">We have 40 years of proven success creating dialogue-based solutions to some of the worlds most entrenched and vexing problems.</p>
    <p class="abs cover-lead center">Our product is a corporate training program called</p>
    <h1 class="abs product-name">Marigold<br>Compass</h1>
    <p class="abs cover-outro center">We have 40 years of proven success creating dialogue-based solutions to some of the worlds most entrenched and vexing problems.</p>
  </article>

</main>
</body>
</html>
```